Bright Ember Publicity is a new boutique Press Office with a small roster of well-chosen clients across an array of disciplines; from Art and Technology to Restaurants and Fashion. Based in Greenpoint Brooklyn, Bright Ember Publicity achieves outstanding results through hard work, tenacity, efficiency and a sense of humor. We need a simple, versatile and classic design. We would like each side of the card to be white text on a black background.

Boutique

```html
<!DOCTYPE html>
<html lang="en">
<head>
<meta charset="utf-8">
<title>Bright Ember Publicity — Business Card</title>
<link href="https://fonts.googleapis.com/css2?family=Bodoni+Moda:wght@500&family=Arimo:wght@400;700&display=swap" rel="stylesheet">
<style>
  :root {
    --stage: #8a8a8a;
    --stage-edge: #2a2a2a;
    --card: #0d0d0d;
    --card-sheen: #1c1c1c;
    --ink: #ffffff;
    --ink-soft: #c9c9c9;
    --rule: #5a5a5a;
    --wave-grey: #8e8e8e;
    --wave-light: #f2f2f2;
  }
  * { margin: 0; padding: 0; box-sizing: border-box; }
  html, body { width: 1200px; height: 950px; overflow: hidden; }
  body {
    background: radial-gradient(ellipse at 50% 45%, var(--stage) 0%, #555 45%, var(--stage-edge) 100%);
    position: relative;
    font-family: "Arimo", Arial, sans-serif;
  }
  .card {
    position: absolute;
    width: 630px;
    height: 360px;
    background: linear-gradient(135deg, var(--card-sheen) 0%, var(--card) 55%);
    box-shadow: 0 18px 40px rgba(0,0,0,.55);
    overflow: hidden;
    color: var(--ink);
  }
  /* front */
  .card-front { left: 80px; top: 80px; }
  .front-name {
    position: absolute; left: 0; right: 0; top: 120px;
    text-align: center;
    font-family: "Bodoni Moda", "Times New Roman", serif;
    font-weight: 500; font-size: 46px; letter-spacing: 1px;
  }
  .front-web {
    position: absolute; left: 0; right: 0; top: 240px;
    text-align: center; font-size: 14px; letter-spacing: 5px; color: var(--ink-soft);
  }
  /* back */
  .card-back { left: 490px; top: 510px; }
  .wave { position: absolute; left: 0; top: 0; width: 630px; height: 360px; }
  .brand {
    position: absolute; right: 40px; top: 44px; width: 300px; text-align: center;
    font-family: "Bodoni Moda", "Times New Roman", serif; font-weight: 500;
  }
  .brand-name { font-size: 26px; letter-spacing: 2px; line-height: 1.15; }
  .brand-rule { position: absolute; left: 0; right: 40px; top: 142px; height: 1px; background: var(--rule); }
  .address {
    position: absolute; right: 40px; top: 156px; text-align: right;
    font-size: 13px; line-height: 19px; color: var(--ink);
  }
  .address .web { letter-spacing: 2px; }
  .person { position: absolute; left: 38px; top: 212px; }
  .person-name { font-size: 19px; font-weight: 700; }
  .person-role { font-size: 13px; color: var(--ink-soft); margin-top: 3px; }
  .person-rule { width: 140px; height: 1px; background: var(--rule); margin: 8px 0 6px; }
  .contacts { list-style: none; font-size: 13px; }
  .contacts li { display: flex; align-items: center; gap: 10px; height: 20px; }
  .contacts svg { width: 14px; height: 14px; fill: var(--ink); flex: none; }
</style>
</head>
<body>

<section class="card card-front" aria-label="Card front">
  <div class="front-name">Bright Ember Publicity</div>
  <div class="front-web">www.brightember.com</div>
</section>

<section class="card card-back" aria-label="Card back">
  <svg class="wave" viewBox="0 0 630 360" aria-hidden="true">
    <path d="M250 360 C 390 335, 480 262, 630 240 L630 360 Z" fill="var(--wave-grey)"/>
    <path d="M305 360 C 430 340, 515 285, 630 268 L630 360 Z" fill="var(--wave-light)"/>
  </svg>

  <div class="brand">
    <div class="brand-name">Bright Ember<br>Publicity</div>
  </div>
  <div class="brand-rule"></div>

  <div class="address">
    417 Calloway Street<br>
    Greenpoint, NY 11222<br>
    <span class="web">www.brightember.com</span>
  </div>

  <div class="person">
    <div class="person-name">Mara Lindell</div>
    <div class="person-role">President</div>
    <div class="person-rule"></div>
    <ul class="contacts">
      <li><svg viewBox="0 0 16 16"><path d="M3 1h3l1.5 4-2 1.3a9 9 0 0 0 4.2 4.2L11 8.5l4 1.5v3a2 2 0 0 1-2 2A12 12 0 0 1 1 3a2 2 0 0 1 2-2z"/></svg>555 0142 7731</li>
      <li><svg viewBox="0 0 16 16"><path d="M4 0h8a1 1 0 0 1 1 1v14a1 1 0 0 1-1 1H4a1 1 0 0 1-1-1V1a1 1 0 0 1 1-1zm1 2v10h6V2zm3 11a1 1 0 1 0 0 2 1 1 0 0 0 0-2z"/></svg>555 0198 2264</li>
      <li><svg viewBox="0 0 16 16"><path d="M4 1h8v4h2v8h-2v2H4v-2H2V5h2zm1 1v3h6V2zm0 8v4h6v-4z"/></svg>555 0176 4410</li>
      <li><svg viewBox="0 0 16 16"><path d="M1 3h14v10H1zm1.5 1.2V12h11V4.2L8 8.5z"/></svg>mara@brightember.com</li>
    </ul>
  </div>
</section>

</body>
</html>
```